eBook opt in for website

I write short ebooks (2500 words) to give free as an opt in. I need a cover design with block headers within the pages to highlight the specifics sections for PDF.
Book Title:
Harbor Compass Method
Sharpen Every Crew Bond Using Five Quiet Habits
I would like to see a design for the front cover that would emphasize a leader's personal growth to team.
The color that comes to mind is blue.
I do have a Brand Design and Icon if you need it.

Target Market(s)
Leaders with Team Responsibility
Industry/Entity Type
Business Consultant
Look and feel

```html
<!DOCTYPE html>
<html lang="en">
<head>
<meta charset="utf-8">
<title>Harbor Compass Method — eBook Cover</title>
<link rel="stylesheet" href="https://fonts.googleapis.com/css2?family=Antonio:wght@400&family=Questrial&display=swap">
<style>
  :root {
    --page-bg: #f1f2f3;
    --cover-deep: #1f86c9;
    --cover-mid: #3aa2dc;
    --cover-light: #58b6e6;
    --band-tint: rgba(255, 255, 255, 0.16);
    --strip: #1d7ec0;
    --title-cyan: #43f0fb;
    --subtitle-yellow: #f6f39a;
    --numeral: #1a5f9c;
    --badge-line: #ffffff;
  }
  * { margin: 0; padding: 0; box-sizing: border-box; }
  html, body {
    width: 1200px;
    height: 1000px;
    overflow: hidden;
    background: var(--page-bg);
  }
  .cover {
    position: absolute;
    left: 297px;
    top: 37px;
    width: 605px;
    height: 806px;
    overflow: hidden;
    background: var(--cover-mid);
  }
  .cover__photo {
    position: absolute;
    inset: 0;
    background:
      radial-gradient(ellipse at 45% 55%, rgba(20, 70, 120, 0.35), transparent 60%),
      linear-gradient(160deg, var(--cover-light) 0%, var(--cover-mid) 45%, var(--cover-deep) 100%);
  }
  .cover__band {
    position: absolute;
    left: 0;
    top: 315px;
    width: 100%;
    height: 476px;
    background: var(--band-tint);
  }
  .cover__strip {
    position: absolute;
    left: 0;
    bottom: 0;
    width: 100%;
    height: 15px;
    background: var(--strip);
  }
  .title {
    position: absolute;
    left: 0;
    top: 38px;
    width: 100%;
    text-align: center;
    font-family: "Antonio", "Arial Narrow", sans-serif;
    font-weight: 400;
    color: var(--title-cyan);
    text-transform: uppercase;
    line-height: 1;
    white-space: nowrap;
  }
  .title__line { display: block; }
  .title__line--top { font-size: 84px; letter-spacing: 1px; }
  .title__line--bottom { font-size: 116px; letter-spacing: 16px; margin-top: 12px; padding-left: 16px; }
  .subtitle {
    position: absolute;
    left: 0;
    top: 332px;
    width: 100%;
    text-align: center;
    font-family: "Questrial", "Century Gothic", sans-serif;
    color: var(--subtitle-yellow);
    line-height: 1;
    font-weight: 400;
  }
  .subtitle__line { display: block; }
  .subtitle__lead { font-size: 42px; }
  .subtitle__key { font-size: 104px; margin-top: 4px; letter-spacing: 1px; }
  .subtitle__key--second { font-size: 44px; margin-top: 4px; text-transform: uppercase; }
  .subtitle__join { font-size: 31px; margin-top: 18px; }
  .numeral {
    position: absolute;
    left: 310px;
    top: 595px;
    font-family: "Questrial", "Century Gothic", sans-serif;
    font-size: 200px;
    line-height: 1;
    color: var(--numeral);
    opacity: 0.75;
  }
  .subtitle__close {
    position: absolute;
    left: 0;
    top: 663px;
    width: 100%;
    text-align: center;
    font-family: "Questrial", "Century Gothic", sans-serif;
    font-size: 70px;
    line-height: 1;
    color: var(--subtitle-yellow);
  }
  .author-badge {
    position: absolute;
    left: 455px;
    top: 540px;
    width: 110px;
    height: 110px;
    border: 1.5px solid var(--badge-line);
    border-radius: 50%;
    display: flex;
    align-items: center;
    justify-content: center;
    text-align: center;
    font-family: "Questrial", "Century Gothic", sans-serif;
    font-size: 15px;
    line-height: 1.2;
    color: var(--badge-line);
  }
</style>
</head>
<body>
  <main class="cover">
    <div class="cover__photo" role="img" aria-label="Close-up photograph of chess pieces on a board, tinted blue"></div>
    <div class="cover__band"></div>
    <div class="cover__strip"></div>

    <h1 class="title">
      <span class="title__line title__line--top">Harbor Compass</span>
      <span class="title__line title__line--bottom">Method</span>
    </h1>

    <p class="numeral" aria-hidden="true">5</p>

    <h2 class="subtitle">
      <span class="subtitle__line subtitle__lead">Sharpen Every</span>
      <span class="subtitle__line subtitle__key">CREW</span>
      <span class="subtitle__line subtitle__key--second">Bond</span>
      <span class="subtitle__line subtitle__join">Using Five Quiet</span>
    </h2>
    <p class="subtitle__close">Habits</p>

    <div class="author-badge">Maren<br>Holloway</div>
  </main>
</body>
</html>
```